FACIAL COSMETICS BUSINESS CARD

WE ARE A DENTAL PRACTICE BUT ARE OPENING UP A BRANCH FOR FACILA COSMETICS, LIKE BOTOX, FILLERS, PEELS, ETC. MAEVE AND ISOLDA WILL BE RUNNING THAT PART OF THE BUSINESS.
OUR CURRENT CARD IS ATTACHED AND OUR LOGO IT ATTACHED TOO. THE LOGO HAS ON IT OVEN DENTAL, I WOULD LIKE IT TO SAY OVEN COSMETICS, THE PHONE NUMBERS ON IT HAS TO BE REPLACED BY THE ONES I GAVE PREVIOUSLY AND THE WEB ADDRESS HAS TO BE DELETED, THE OTHER SIDE OF THE CARD HAS A MAP WHICH HAS TO BE DELETED, ADD TWO DATE-TIME LINES, I LIKE THE CARDS TO BE SIMPLE AND CLEAN, SIZE HAS TO BE NO LARGER THAN 5CMx8.5CM.
THE CARD HAS TO BE MATTE, I HATE GLOSSY, ABLE TO BE WRITTEN ON BOTH SIDES

Updates
I HAVE ATTACHED THE FILES, THEY CONSIST OF OUR CURRENT LOGO IN A FEW FORMS AND OUR BUSINESS CARD FOR THE DENTAL BRANCH, PLEASE COPY THE CURRENT DESIGN BUT ADDING THE REQUESTED CHANGES

Industry/Entity Type
Business
Contact Information for Business Card
OVEN COSMETICS
MAEVE : 0438 572 913
ISOLDA : 0429 638 207
SUITE 8 COLWOOD PARK ARCADE
74-86 HALBERT STREET
COLWOOD PARK NSW 2284
Logo Text
OVEN COSMETICS
Look and feel

```html
<!DOCTYPE html>
<html lang="en">
<head>
<meta charset="utf-8">
<title>Oven Cosmetics – Business Card</title>
<link rel="stylesheet" href="https://fonts.googleapis.com/css2?family=Source+Sans+3:wght@400;600;700&display=swap">
<style>
  :root {
    --backdrop: #d9d9d9;
    --card: #ffffff;
    --ink: #262626;
    --rule: #333333;
    --brand-green: #5cb83f;
    --ornament-light: #f2f2f2;
    --ornament-mid: #e2e2e2;
  }
  * { box-sizing: border-box; margin: 0; padding: 0; }
  html, body {
    width: 1200px; height: 900px; overflow: hidden;
    background: var(--backdrop);
    font-family: "Source Sans 3", Arial, sans-serif;
    color: var(--ink);
  }
  .sheet {
    position: relative; width: 1200px; height: 900px;
    display: flex; align-items: center; justify-content: center; gap: 60px;
  }
  .card {
    position: relative; width: 510px; height: 300px;
    background: var(--card);
    box-shadow: 0 6px 18px rgba(0,0,0,0.18);
    overflow: hidden;
  }
  .ornament {
    position: absolute;
    background: radial-gradient(ellipse at center, var(--ornament-mid) 0%, var(--ornament-light) 55%, rgba(255,255,255,0) 80%);
  }
  .card-front .ornament { left: 20px; top: 40px; width: 470px; height: 220px; }
  .card-back .ornament { left: 250px; top: 10px; width: 260px; height: 220px; }

  .brand {
    position: absolute; display: flex; align-items: center; gap: 10px;
  }
  .brand-dot {
    width: 16px; height: 16px; border-radius: 50%;
    background: var(--brand-green); flex: none;
  }
  .brand-name {
    font-weight: 600; color: var(--ink); letter-spacing: 0.06em;
    white-space: nowrap; line-height: 1;
  }
  .card-front .brand { left: 50%; top: 50%; transform: translate(-50%, -50%); }
  .card-front .brand-name { font-size: 28px; }
  .card-back .brand { left: 30px; bottom: 62px; }
  .card-back .brand-name { font-size: 24px; }

  .write-line {
    position: absolute; top: 30px;
    display: flex; align-items: flex-end; gap: 6px;
    font-size: 9px; font-weight: 700; letter-spacing: 0.08em;
  }
  .write-line span.line { display: block; height: 1px; background: var(--rule); margin-bottom: 2px; }
  .date-line { left: 26px; }
  .date-line .line { width: 160px; }
  .time-line { left: 270px; }
  .time-line .line { width: 170px; }

  .address {
    position: absolute; right: 40px; top: 62px;
    text-align: right; font-weight: 700; font-size: 14.5px; line-height: 1.25;
  }
  .phones {
    position: absolute; right: 40px; top: 162px;
    text-align: right; font-size: 15px; line-height: 1.45;
  }
  .phones b { font-weight: 700; letter-spacing: 0.03em; }
</style>
</head>
<body>
<main class="sheet">
  <section class="card card-front" aria-label="Card front">
    <div class="ornament" role="img" aria-label="Faint grey flourish pattern"></div>
    <div class="brand">
      <span class="brand-dot"></span>
      <span class="brand-name">OVEN COSMETICS</span>
    </div>
  </section>

  <section class="card card-back" aria-label="Card back">
    <div class="ornament" role="img" aria-label="Faint grey flourish pattern"></div>
    <div class="write-line date-line">DATE <span class="line"></span></div>
    <div class="write-line time-line">TIME <span class="line"></span></div>
    <address class="address" style="font-style:normal">
      Suite 8<br>
      Colwood Park Arcade<br>
      74-86 Halbert Street<br>
      Colwood Park, NSW 2284
    </address>
    <div class="phones">
      <div><b>MAEVE:</b> 0438 572 913</div>
      <div><b>ISOLDA:</b> 0429 638 207</div>
    </div>
    <div class="brand">
      <span class="brand-dot"></span>
      <span class="brand-name">OVEN COSMETICS</span>
    </div>
  </section>
</main>
</body>
</html>
```